WP website design for Pelton

We need a wordpress design that will incorporate a professional color scheme with company logo in a clean layout. The design needs to consider that this will be developed on a responsive theme. Colors are will be the green of the logo and any others that will creatively highlight it.

Industry/Entity Type

It Company

Font styles to use
Sans Serif

Requirements
Must have
• Navigation: 1) Home 2) Auctions 3) Auction Services 4) Sellers 5) RK Pelton Livestock 6) About Us 7) Contact Us
Site will have slideshow element, image attached.
Widgets will be: 1)Email Signup form 2) Featured Auctions widget 3) Social Media (Chirply, Vidloop, RSS) 4) News & Events blog
Footer will have smaller company logo, association logos (attached) and contact info (below)
▪ R.K. Pelton Inc. / Auctioneers
▪ 4716 NC Hwy 91
▪ Marbury, NC 27604
▪ Office: (252) 555-0184
▪ Cell: (252) 555-0137
▪ email: rkpelton@rkpelton-example.com
Nice to have
• Site will have drop-down menus - please indicate the styling, for instance the dropdown menus

```html
<!DOCTYPE html>
<html lang="en">
<head>
<meta charset="utf-8">
<title>R.K. Pelton Inc. / Auctioneers — Mobile Home</title>
<link rel="stylesheet" href="https://fonts.googleapis.com/css2?family=Open+Sans:wght@400;600&family=Arimo:wght@700&family=Cormorant+Garamond:ital,wght@1,600&display=swap">
<style>
  :root {
    --brand-green: #2f8417;
    --brand-green-dark: #26700f;
    --logo-green: #2e8b12;
    --canvas-bg: #e6e9e4;
    --screen-bg: #ffffff;
    --panel-bg: #ececec;
    --panel-bg-light: #f4f4f4;
    --text-body: #2b2b2b;
    --rule: #bdbdbd;
    --menu-arrow: #d62222;
    --chirply: #3b5a98;
    --vidloop: #c4302b;
    --rss: #3f9a1a;
    --photo-sky: #a9cde8;
    --photo-haze: #d9e6d2;
    --photo-field: #a9c27a;
  }

  * { box-sizing: border-box; margin: 0; padding: 0; }

  html, body {
    width: 1130px;
    height: 1200px;
    overflow: hidden;
    background: var(--canvas-bg);
    font-family: "Open Sans", Arial, sans-serif;
  }

  .screen {
    position: absolute;
    left: 197px;
    top: 0;
    width: 736px;
    height: 1200px;
    background: var(--screen-bg);
    overflow: hidden;
  }

  /* Header */
  .site-header {
    position: relative;
    height: 363px;
  }

  .brand {
    position: absolute;
    left: 124px;
    top: 70px;
    width: 484px;
    text-align: center;
    color: var(--logo-green);
    font-weight: 600;
    line-height: 1.15;
  }
  .brand-name { display: block; font-size: 78px; }
  .brand-tag  { display: block; font-size: 50px; margin-top: 22px; }

  .social {
    position: absolute;
    right: 20px;
    top: 46px;
    list-style: none;
    text-align: center;
    font-size: 24px;
    font-weight: 600;
    line-height: 1;
  }
  .social li { margin-bottom: 34px; }
  .social .chirply { color: var(--chirply); }
  .social .vidloop { color: var(--vidloop); }
  .social .rss     { color: var(--rss); }

  /* Navigation */
  .main-nav {
    position: relative;
    height: 85px;
    background: var(--brand-green);
    display: flex;
    align-items: center;
    padding-left: 46px;
  }
  .main-nav .current {
    color: #fff;
    font-size: 37px;
    letter-spacing: 0.5px;
  }
  .menu-toggle {
    position: absolute;
    right: 36px;
    top: 16px;
    width: 54px;
    height: 54px;
    background: #fff;
    border: 2px solid #d9d9d9;
  }
  .menu-toggle svg { display: block; width: 100%; height: 100%; }

  /* Featured auctions widget */
  .featured {
    margin: 7px 28px 0;
  }
  .featured-heading {
    height: 113px;
    background: var(--brand-green);
    color: #fff;
    font-family: "Cormorant Garamond", Georgia, serif;
    font-style: italic;
    font-weight: 600;
    font-size: 70px;
    text-align: center;
    line-height: 113px;
    text-shadow: 2px 3px 3px rgba(0,0,0,0.55);
    letter-spacing: 0.5px;
  }
  .auction-photo {
    height: 306px;
    background:
      linear-gradient(180deg, var(--photo-sky) 0%, var(--photo-haze) 60%, var(--photo-field) 100%);
  }
  .auction-card {
    background: linear-gradient(180deg, var(--panel-bg) 0%, var(--panel-bg-light) 100%);
    padding: 8px 62px 40px;
    min-height: 420px;
  }
  .auction-title {
    color: var(--brand-green);
    font-weight: 400;
    font-size: 46px;
    line-height: 1.15;
  }
  .auction-summary {
    color: var(--text-body);
    font-size: 29.5px;
    line-height: 37px;
    padding-bottom: 14px;
    border-bottom: 2px solid var(--rule);
  }
  .auction-meta {
    margin-top: 16px;
    font-family: "Arimo", Arial, sans-serif;
    font-weight: 700;
    font-size: 31px;
    color: var(--brand-green-dark);
  }
</style>
</head>
<body>
  <div class="screen">
    <header class="site-header">
      <div class="brand">
        <span class="brand-name">R.K. Pelton</span>
        <span class="brand-tag">Inc. / Auctioneers</span>
      </div>
      <ul class="social">
        <li class="chirply">Chirply</li>
        <li class="vidloop">Vidloop</li>
        <li class="rss">RSS</li>
      </ul>
    </header>

    <nav class="main-nav">
      <span class="current">HOME</span>
      <span class="menu-toggle" aria-label="Open menu">
        <svg viewBox="0 0 54 54" aria-hidden="true">
          <polygon points="13,17 41,17 27,38" fill="var(--menu-arrow)"/>
        </svg>
      </span>
    </nav>

    <section class="featured">
      <h2 class="featured-heading">Featured Auctions</h2>
      <div class="auction-photo" role="img" aria-label="Photo of two brown horses galloping across a sunlit field"></div>
      <article class="auction-card">
        <h3 class="auction-title">Auction Title</h3>
        <p class="auction-summary">Lorem Ipsum. Proin gravida nibh vel velit auctor aliquet. Aenean sollicitudin, lorem quis bibendum auctor, nisi elit consequat ipsum, nec sagittis sem nibh id elit..</p>
        <p class="auction-meta">Begins:</p>
      </article>
    </section>
  </div>
</body>
</html>
```